Web Design Project for Brantley Harbor Advisors, LP

We are looking for a new website for Brantley Harbor Advisors, LP an investment management (alternative investment) firm with offices in New York, NY and Seattle, WA. We are looking for designs utilizing gray, blue and white, corresponding with our logo. Our current website is www.brantleyharborllc.example.

Some websites with the feel we are looking for:

http://quillbrookfunds.example/cgi-bin/index.pl
http://www.tessendalp.example/

Target Market(s)

wealthy individuals and large investors

Industry/Entity Type

Investment

Requirements
Must have
• A couple/few page website, utilizing the below text & contact info and use one of the logos that are attached.

Text to be inlcuded:

Brantley Harbor Advisors, LP is a hedge fund manager responsible for a multi-strategy fund primarily implementing a long/short equity strategy and utilizing macro, credit, event driven and distressed strategies while maintaining a market neutral portfolio.

The Fund seeks to achieve absolute returns while minimizing risk with particular attention paid to preserving capital.

Contact information to be included:

East Coast:

417 Corwin Street #608
New York, NY 10093
Phone : +1 212.555.0147
Fax : +1 212.555.0183
info@brantleyharborllc.example

West Coast:

3871 Halvern Street #524
Seattle, WA 98190
info@brantleyharborllc.example
Should not have
• anything too flashy

```html
<!DOCTYPE html>
<html lang="en">
<head>
<meta charset="utf-8">
<title>Brantley Harbor Advisors, LP</title>
<link href="https://fonts.googleapis.com/css2?family=Cinzel:wght@400;500&family=Arimo:wght@400&display=swap" rel="stylesheet">
<style>
:root{
  --page-blue:#003478;
  --brand-blue:#0d3a80;
  --link-blue:#0a2f74;
  --ink:#333;
  --body-gray:#555;
  --nav-top:#7a7a7a;
  --nav-bottom:#4a4a4a;
  --footer-bg:#eeeff1;
}
*{margin:0;padding:0;box-sizing:border-box}
html,body{width:1200px;height:1010px;overflow:hidden}
body{background:var(--page-blue);font-family:Arimo,Arial,sans-serif;color:var(--ink)}
.page{position:absolute;left:120px;top:0;width:960px;height:1010px;background:#fff}
.brand{position:absolute;left:30px;top:34px;font-family:Cinzel,serif;font-weight:500;color:var(--brand-blue);font-size:26px;line-height:30px;letter-spacing:1px}
.header-phone{position:absolute;left:718px;top:47px;display:flex;align-items:center;gap:12px;font-size:24px;color:var(--ink)}
.header-phone svg{display:block}
.main-nav{position:absolute;left:30px;top:123px;width:900px;height:37px;border-radius:4px;background:linear-gradient(var(--nav-top),#5c5c5c 50%,var(--nav-bottom));border:1px solid #444;display:flex;align-items:center}
.main-nav a{color:#fff;text-decoration:none;font-size:14px;height:100%;display:flex;align-items:center;justify-content:center;border-right:1px solid #3c3c3c;box-shadow:1px 0 0 #888}
.search{position:absolute;right:16px;top:6px;display:flex;align-items:center;gap:6px;color:#fff;font-size:14px}
.search-box{width:147px;height:23px;background:#fff;border-radius:5px;position:relative}
.search-box svg{position:absolute;right:4px;top:3px}
.hero{position:absolute;left:30px;top:180px;width:900px;height:324px;border-radius:6px;overflow:hidden;border:1px solid #ccc;background:linear-gradient(100deg,#d9dde2 0%,#eef0f2 35%,#c8b8ab 55%,#2a2a2e 70%,#e6e4e0 85%,#cfc6bb 100%)}
.hero-band{position:absolute;left:0;top:192px;width:400px;height:92px;background:linear-gradient(90deg,rgba(40,40,40,.75),rgba(60,60,60,.55) 80%,rgba(60,60,60,0))}
.hero-line1{position:absolute;left:25px;top:200px;color:#fff;font-size:28px;text-shadow:1px 1px 2px rgba(0,0,0,.5)}
.hero-line1 .big{font-size:38px}
.hero-line2{position:absolute;left:145px;top:237px;color:#fff;font-size:26px;text-shadow:1px 1px 2px rgba(0,0,0,.5)}
.welcome{position:absolute;left:30px;top:541px;font-family:Cinzel,serif;font-size:22px;font-weight:400;color:var(--ink)}
.welcome span{color:var(--brand-blue)}
.intro{position:absolute;left:30px;top:603px;width:598px;font-size:14px;line-height:17px;color:var(--body-gray);text-align:justify}
.intro p{margin-bottom:16px}
.divider{position:absolute;left:688px;top:535px;width:10px;height:370px;background:linear-gradient(90deg,rgba(0,0,0,.12),rgba(0,0,0,0));-webkit-mask:linear-gradient(transparent,#000 15%,#000 85%,transparent);mask:linear-gradient(transparent,#000 15%,#000 85%,transparent)}
.contact{position:absolute;left:735px;top:541px;width:210px;font-size:14px;color:var(--body-gray)}
.contact h2{font-family:Cinzel,serif;font-weight:400;font-size:22px;color:var(--brand-blue);margin-bottom:30px}
.contact h3{font-weight:400;font-size:18px;color:var(--ink);margin-bottom:12px}
.contact p{line-height:17px}
.contact .row{margin-top:7px}
.contact a{color:var(--link-blue);text-decoration:none}
.contact .office+.office{margin-top:30px}
.site-footer{position:absolute;left:0;top:953px;width:960px;height:57px;background:var(--footer-bg);border-top:1px solid #ccc;display:flex;align-items:center;justify-content:center;font-size:14px;color:#222}
</style>
</head>
<body>
<div class="page">
  <header>
    <div class="brand">Brantley Harbor<br>Advisors, LP</div>
    <div class="header-phone">
      <svg width="34" height="34" viewBox="0 0 34 34" aria-hidden="true"><rect width="34" height="34" rx="5" fill="#0d3a80"/><path d="M12 7c2 0 3 3 3.5 5 .3 1-1.5 2-1.5 2 0 3 2 7 4 9 0 0 1.5-1.2 2.5-.6 1.8 1 3.8 2.4 3.5 4-.4 2-3 3-5 2.5C13 27 9 19 9 12c0-2 1-5 3-5z" fill="#fff"/></svg>
      <span>1 212.555.0147</span>
    </div>
  </header>
  <nav class="main-nav">
    <a href="#" style="width:87px">Home</a>
    <a href="#" style="width:98px">About Us</a>
    <a href="#" style="width:99px">Services</a>
    <a href="#" style="width:99px">Solutions</a>
    <a href="#" style="width:119px">Testimonials</a>
    <a href="#" style="width:113px">Contact Us</a>
    <div class="search">Search
      <div class="search-box"><svg width="18" height="17" viewBox="0 0 18 17" aria-hidden="true"><circle cx="7" cy="7" r="5" fill="none" stroke="#666" stroke-width="2"/><path d="M11 11l5 5" stroke="#666" stroke-width="3" stroke-linecap="round"/></svg></div>
    </div>
  </nav>
  <section class="hero" role="img" aria-label="Photo of smiling business professionals in a bright office">
    <div class="hero-band"></div>
    <div class="hero-line1"><span class="big">WE</span> CAN BE YOUR GUIDE</div>
    <div class="hero-line2">in the world of finance!</div>
  </section>
  <h1 class="welcome">Welcome to <span>Brantley Harbor Advisors</span></h1>
  <div class="intro">
    <p>Brantley Harbor Advisors, LP is a hedge fund manager responsible for a multi-strategy fund primarily implementing a long/short equity strategy and utilizing macro, credit, event driven and distressed strategies while maintaining a market neutral portfolio.</p>
    <p>The Fund seeks to achieve absolute returns while minimizing risk with particular attention paid to preserving capital.</p>
  </div>
  <div class="divider"></div>
  <aside class="contact">
    <h2>Contact Us</h2>
    <div class="office">
      <h3>East Coast:</h3>
      <p>417 Corwin Street #608<br>New York, NY 10093</p>
      <p class="row">Phone : <a href="#">+1 212.555.0147</a></p>
      <p class="row">Fax : <a href="#">+1 212.555.0183</a></p>
      <p class="row">Email : <a href="#">info@brantleyharborllc.example</a></p>
    </div>
    <div class="office">
      <h3>West Coast:</h3>
      <p>3871 Halvern Street #524<br>Seattle, WA 98190</p>
      <p class="row">Email : <a href="#">info@brantleyharborllc.example</a></p>
    </div>
  </aside>
  <footer class="site-footer">copyright 2010-2012. Brantley Harbor, LLC. All rights reserved.</footer>
</div>
</body>
</html>
```